Landing Page Design Needed For Lead Generation capture.

We are a lead / appointment service specifically for the custom closet systems industry. We need a landing page created for a Wix site.
We need the winner to code the site for a Wix platform.
Winner will earn ongoing business.

The domain name format will be this format: www.RackNomad{City}.com
For example this first landing page is www.RackNomadGreenville.com
When we add new cities we will create new landing pages.

Rack Nomad Greenville will be the name of this first landing page so a simple logo is needed.

View this website first: www.HangarWerks.com for inspiration and to learn about custom closet systems.

You can also use this site for copy inspiration and photo examples. Also the form is similar to what we need. (Must also be mobile optimized)

A slider showing showing the following would be helpful:

Our value and service.

Rack Nomad Greenville pre screens custom closet companies and matches home owners with the best company in their area / zip code. This saves home owners both time and money. Let Rack Nomad make it easy for you!

On the page, tell the visitor to use promo code NOMA500 to save $500 off any size closet system.

Here are names and descriptions for the slider photos:

1. Bedroom Closet - Closets as unique as you
2. Entertainment Center - Artfully entertaining
3. Laundry room - Make doing laundry FUN!
4. Home office - Make working from home smarter
5. Garage - Park in your garage again and find everything the first time!

The form should have the following fields.

"Schedule your free consultation with our pre screened closet designers"
- First and Last Name
- Email
- Phone
- Zip
(A check box for the following allowing multiple selections)
"I'm Interested In"
1. Bedroom Closet
2. Entertainment Center
3. Laundry room
4. Home office
5. Garage system

"Enter Promo Code"

Text at the bottom of the form:
"We use your zip code to align you with the nearest and best closet designers. We use your email and phone number to contact you and schedule your free design consultation."

The data from the submitted form will go to: leeds@RackNomadGreenville.com

Target Market(s)

Home owners

Coding

```html
<!DOCTYPE html>
<html lang="en">
<head>
<meta charset="utf-8">
<title>Rack Nomad Greenville</title>
<link href="https://fonts.googleapis.com/css2?family=Crimson+Text:wght@400;600;700&display=swap" rel="stylesheet">
<style>
:root{
  --plum:#9e4f69;
  --ink:#111111;
  --white:#ffffff;
  --field-border:#c9d3dc;
  --rule:#cccccc;
  --brown:#9a6a35;
  --badge:#d9d9d9;
}
*{box-sizing:border-box;margin:0;padding:0}
html,body{width:1200px;height:1007px;overflow:hidden;background:var(--white);font-family:"Crimson Text",serif;color:var(--ink)}
.promo-bar{height:35px;background:var(--plum);color:var(--white);font-size:14px;display:flex;align-items:center;justify-content:center;letter-spacing:.2px}
.site-header{height:69px;position:relative}
.brand{position:absolute;left:141px;top:16px;display:flex;align-items:center;gap:8px}
.brand-mark{width:18px;height:18px;border-radius:50%;background:var(--brown)}
.brand-name{font-size:28px;font-weight:600;color:var(--brown)}
.contact{position:absolute;top:17px;display:flex;gap:8px;align-items:flex-start}
.contact-phone{left:681px}
.contact-mail{left:843px}
.contact-label{color:var(--plum);font-weight:600;font-size:14px;line-height:16px}
.contact-value{font-size:13.5px;line-height:17px}
.hero{position:relative;height:530px;overflow:hidden}
.hero-photo{position:absolute;inset:0;background:
  linear-gradient(90deg,rgba(40,28,20,.55),rgba(60,45,35,.35) 40%,rgba(80,65,55,.2)),
  linear-gradient(180deg,#cbb9a5 0%,#8d7a68 35%,#6e5d50 60%,#a8988a 100%)}
.hero-title{position:absolute;left:140px;top:222px;color:var(--white)}
.hero-title h1{font-size:42px;font-weight:600;letter-spacing:.5px;line-height:46px}
.hero-title p{font-size:24px;font-weight:600;margin-top:2px}
.consult-panel{position:absolute;left:720px;top:53px;width:339px;height:424px;background:rgba(200,200,200,.75);padding:7px}
.consult-inner{background:var(--white);height:100%}
.consult-head{background:#000;color:var(--white);text-align:center;height:68px;padding-top:8px}
.consult-head h2{font-size:20.5px;font-weight:600;line-height:24px;letter-spacing:.2px}
.consult-head p{font-size:15px;line-height:18px}
.consult-form{padding:11px 7px 0}
.field{height:35px;border:1px solid var(--field-border);font-size:11px;padding-left:7px;display:flex;align-items:center;margin-bottom:11px;background:var(--white)}
.row{display:flex;gap:9px}
.row .field{flex:1}
.select{justify-content:space-between;padding-right:10px}
.promo-row{display:flex;gap:8px}
.promo-row .field{width:212px}
.submit{width:91px;height:35px;background:var(--plum);color:var(--white);font-size:15px;font-weight:600;letter-spacing:.5px;display:flex;align-items:center;justify-content:center}
.consult-note{font-size:10.5px;line-height:16px;text-align:center;padding:0 5px;margin-top:-1px}
.about{text-align:center;padding:0 141px}
.about h2{color:var(--plum);font-size:36px;font-weight:600;margin-top:44px;line-height:44px}
.about p{font-size:15px;line-height:26.5px;margin-top:10px}
.site-footer{position:absolute;left:141px;top:938px;width:918px;border-top:1px solid var(--rule);height:69px}
.partner-badge{position:absolute;left:0;top:12px;width:154px;height:44px;border-radius:4px;background:var(--badge)}
.copyright{position:absolute;right:2px;top:24px;font-size:13px}
</style>
</head>
<body>
<div class="promo-bar">Use Promo Code NOMA500 To Save $500 Off Any Size Closet System.</div>
<header class="site-header">
  <div class="brand"><span class="brand-mark"></span><span class="brand-name">Rack Nomad</span></div>
  <div class="contact contact-phone">
    <svg width="28" height="28" viewBox="0 0 28 28" fill="none" stroke="#9e4f69" stroke-width="1.4"><path d="M5 4c-2 2-2 6 2 11s9 9 12 9c2 0 3-1 4-2l-4-4-3 2c-2-1-5-4-6-6l2-3-4-4z"/><circle cx="21" cy="7" r="5"/><path d="M18.5 7l2 2 3-3.5"/></svg>
    <div><div class="contact-label">Call Us</div><div class="contact-value">+1 555 014 2290</div></div>
  </div>
  <div class="contact contact-mail">
    <svg width="30" height="28" viewBox="0 0 30 28" fill="none" stroke="#9e4f69" stroke-width="1.4"><path d="M2 11l13-9 13 9v15H2z"/><path d="M2 11l13 9 13-9"/><path d="M6 8h18M8 12h14"/></svg>
    <div><div class="contact-label">Email Us</div><div class="contact-value">info@racknomadgreenville.com</div></div>
  </div>
</header>
<section class="hero">
  <div class="hero-photo" role="img" aria-label="Walk-in bedroom closet with white shelving, hanging clothes, folded linens and shoes"></div>
  <div class="hero-title"><h1>BEDROOM</h1><p>Closets As Unique As You</p></div>
  <div class="consult-panel">
    <div class="consult-inner">
      <div class="consult-head"><h2>Schedule Your Free Consultation</h2><p>With Our Pre Screened Closet Designers</p></div>
      <div class="consult-form">
        <div class="field">First name</div>
        <div class="field">Last name</div>
        <div class="row"><div class="field">Phone</div><div class="field">Email</div></div>
        <div class="field">City / Zip Coad</div>
        <div class="field select">I'm Interested In <svg width="8" height="6" viewBox="0 0 8 6"><path d="M1 5l3-3 3 3" stroke="#111" stroke-width="1.6" fill="none"/></svg></div>
        <div class="promo-row"><div class="field">Enter Promo Code</div><div class="submit">SUBMIT</div></div>
        <p class="consult-note">We use your zip code to align you with the nearest and best closet designers. We use your email and phone number to contact you and schedule your free design consultation.</p>
      </div>
    </div>
  </div>
</section>
<section class="about">
  <h2>The Rack Nomad KNOWS!</h2>
  <p>The Rack Nomad simplifies your search for the perfect custom closet. We've meticulously sifted through thousands of customer and employee reviews on reviewhall.com to identify the premier custom closet designers nationwide. Our selection isn't just based on cost, but also on the quality of customer service and employee satisfaction, ensuring you receive unparalleled value. With The Rack Nomad you'll have access to a wide range of options, competitive pricing, and exceptional service without going through multiple long hour visits from un vetted designers. Plus, you can trust that your chosen closet company will be there for you long after the sale, whether you require additional service or want to expand your closet system. Choose The Rack Nomad for an effortless, top-tier custom closet experience.</p>
</section>
<footer class="site-footer">
  <div class="partner-badge" role="img" aria-label="Local city partner badge"></div>
  <div class="copyright">© 2024 Rack Nomad Greenville. All Rights Reserved.</div>
</footer>
</body>
</html>
```